Deactivated Coal-Fired Power Plant to be redeveloped into a Green Energy Campus.

Want a striking business card statement that introduces our concept project to provide economic and community recovery to a former rural coal community in western PA.
Essentially 12 project representatives that will lead both the demolition of an existing power plant and the redevelopment to a new Green energy site.
Business Card should reflect our effort.
We are open to ideas.

Target Market(s)

Energy and Power Generation industries

Industry/Entity Type

Power Generation and Data Centers

Contact Information for Business Card

Included in uploaded materials

Font styles to use
Sans Serif
Other font styles liked:
• Arial, Calibri

Requirements
Must have
• Multiple colors

```html
<!DOCTYPE html>
<html lang="en">
<head>
<meta charset="utf-8">
<title>Ridgeline Renewal – Business Card</title>
<link href="https://fonts.googleapis.com/css2?family=Roboto:wght@400;500;900&display=swap" rel="stylesheet">
<style>
  :root {
    --bg: #3a3a3a;
    --card-white: #ffffff;
    --card-black: #1a1a1a;
    --ink: #111111;
    --ink-soft: #444444;
    --green: #1a9a47;
    --divider: #555555;
    --emboss: #8a8a8a;
  }
  * { margin: 0; padding: 0; box-sizing: border-box; }
  html, body {
    width: 1200px; height: 801px; overflow: hidden;
    background: var(--bg);
    font-family: "Roboto", Arial, sans-serif;
  }
  .stage {
    width: 1200px; height: 801px;
    display: flex; align-items: center; justify-content: center; gap: 50px;
  }
  .card {
    width: 520px; height: 297px;
    border-bottom: 4px solid var(--green);
    position: relative;
  }
  .card--front { background: var(--card-white); display: flex; align-items: center; padding: 0 30px; }
  .card--back { background: var(--card-black); display: flex; align-items: center; justify-content: center; }

  .brand { display: flex; align-items: center; gap: 12px; width: 215px; }
  .brand__dot { width: 46px; height: 46px; border-radius: 50%; background: var(--green); flex: none; }
  .brand__name { font-weight: 900; font-size: 22px; line-height: 1.05; color: var(--ink); text-transform: uppercase; }

  .divider { width: 1px; height: 150px; background: var(--divider); margin: 0 22px 0 8px; }

  .contact { color: var(--ink); }
  .contact__name { font-weight: 900; font-size: 19px; letter-spacing: .3px; text-transform: uppercase; }
  .contact__title { font-size: 13px; color: var(--green); margin-top: 3px; }
  .contact__company { font-size: 13px; margin-top: 14px; }
  .contact__list { list-style: none; margin-top: 14px; font-size: 12.5px; color: var(--ink-soft); }
  .contact__list li { display: flex; align-items: center; gap: 7px; margin-top: 3px; }
  .contact__list svg { width: 11px; height: 11px; flex: none; }

  .back-mark { display: flex; align-items: center; gap: 16px; }
  .back-mark__dot { width: 70px; height: 70px; border-radius: 50%; background: linear-gradient(135deg, #c8c8c8, #2a2a2a); }
  .back-mark__name { font-weight: 900; font-size: 30px; text-transform: uppercase; color: var(--emboss); line-height: 1.05; }
</style>
</head>
<body>
<main class="stage">
  <section class="card card--front">
    <div class="brand">
      <span class="brand__dot"></span>
      <span class="brand__name">Ridgeline<br>Renewal</span>
    </div>
    <div class="divider"></div>
    <div class="contact">
      <p class="contact__name">Daniel Harwood</p>
      <p class="contact__title">Chief Operating Officer</p>
      <p class="contact__company">Ridgeline Renewal LLC</p>
      <ul class="contact__list">
        <li><svg viewBox="0 0 12 12"><rect x="3" y="0.5" width="6" height="11" rx="1" fill="none" stroke="#1a9a47" stroke-width="1.3"/></svg>555-014-2200</li>
        <li><svg viewBox="0 0 12 12"><path d="M2 1h3l1 3-1.5 1a7 7 0 0 0 2.5 2.5L8 6l3 1v3a1 1 0 0 1-1 1A9 9 0 0 1 1 2a1 1 0 0 1 1-1z" fill="#1a9a47"/></svg>555-014-2200</li>
        <li><svg viewBox="0 0 12 12"><rect x="0.5" y="2" width="11" height="8" fill="#1a9a47"/><path d="M0.5 2l5.5 4.5L11.5 2" fill="none" stroke="#fff" stroke-width="1"/></svg>dharwood@ridgelinerenewal.com</li>
      </ul>
    </div>
  </section>

  <section class="card card--back">
    <div class="back-mark">
      <span class="back-mark__dot"></span>
      <span class="back-mark__name">Ridgeline<br>Renewal</span>
    </div>
  </section>
</main>
</body>
</html>
```